Harwick Legal

To update and modernize current business card appearance. Marta's business is based in Melbourne with 4 other lawyers in the firm. Marta travels to the Pilbara in Western Australia approximately 1 week a month as part of the firms legal work. She consults with clients in Newman, Tom Price and Port Hedland. The lawyers work mostly from a home office, apart from court appearances. They have a virtual office in Melbourne city, and use facilities in 3 or 4 other locations around Melbourne. It is important the client's think this is a conventional law firm with a permanent office. Our business structure is a difficult concept for them to grasp. The business has been operational for 3 years, growing from 1 lawyer to 4 lawyers during that time. Our website is www.Harwicklegal.example.au and is currently being upgraded as we are not happy with its content. The logo is currently orange and dark grey but the orange is a difficult colour to reproduce and often turns out "poo" brown when documents are printed. We need clients to know we are user friendly and caring - and not head up our rears ends as some lawyers appear to be.
Updates

Thank you for the feedback so far. 1. Some of the designs have too much black (We prefer darker grey & not too much.) 2. Happy for designers to play around with different colours & logo design. What we're after is a modern look and business card that people say "wow" when they pick it up.

Industry/Entity Type

Business

```html
<!DOCTYPE html>
<html lang="en">
<head>
<meta charset="utf-8">
<title>Harwick Legal – Business Card</title>
<link rel="stylesheet" href="https://fonts.googleapis.com/css2?family=Montserrat:wght@400;500;600&family=Oswald:wght@500&display=swap">
<style>
  :root {
    --stage: #e9e7e3;
    --paper: #ffffff;
    --ink: #151515;
    --charcoal: #3a3a3c;
    --slate: #4a4a4c;
    --orange: #f0824a;
    --muted: #555558;
  }
  * { box-sizing: border-box; margin: 0; padding: 0; }
  html, body { width: 1200px; height: 682px; overflow: hidden; }
  body {
    background: var(--stage);
    font-family: "Montserrat", sans-serif;
    color: var(--ink);
    position: relative;
  }
  .card {
    position: absolute;
    left: 110px; top: 66px;
    width: 980px; height: 550px;
    background: var(--paper);
    box-shadow: 0 14px 34px rgba(0,0,0,.22);
    overflow: hidden;
  }
  .card__top-band {
    position: absolute; left: 0; top: 0; width: 100%; height: 30px;
    background: var(--ink);
  }
  .brand {
    position: absolute; left: 70px; top: 90px;
    display: flex; align-items: center; gap: 30px;
  }
  .brand__dot {
    width: 120px; height: 120px; border-radius: 50%;
    background: var(--orange);
  }
  .brand__name {
    font-size: 46px; font-weight: 500; letter-spacing: 6px;
    color: var(--charcoal); text-transform: uppercase;
    padding-bottom: 14px;
    border-bottom: 2px solid var(--charcoal);
  }
  .name-band {
    position: absolute; left: 270px; top: 262px; right: 0; height: 56px;
    background: var(--ink); color: var(--paper);
    display: flex; align-items: center; justify-content: space-between;
    padding: 0 44px 0 28px;
  }
  .name-band__name {
    font-family: "Oswald", sans-serif; font-weight: 500;
    font-size: 34px; letter-spacing: 2px; text-transform: uppercase;
  }
  .name-band__title {
    font-size: 16px; letter-spacing: 3px; text-transform: uppercase;
  }
  .side-block {
    position: absolute; left: 140px; top: 262px; width: 110px; height: 130px;
    background: var(--ink);
    display: flex; align-items: center; justify-content: center;
  }
  .side-accent {
    position: absolute; left: 70px; top: 392px; width: 70px; height: 50px;
    background: var(--orange);
  }
  .contacts {
    position: absolute; left: 290px; top: 340px; right: 40px;
    display: grid; grid-template-columns: 1fr 1fr; row-gap: 16px; column-gap: 30px;
    font-size: 17px; color: var(--muted);
  }
  .contacts__item { display: flex; align-items: center; gap: 14px; }
  .contacts__item svg { flex: none; }
  .address-band {
    position: absolute; left: 0; bottom: 0; width: 100%; height: 86px;
    background: var(--slate); color: var(--paper);
    display: flex; align-items: center; gap: 16px;
    padding-left: 290px; font-size: 18px; letter-spacing: .5px;
  }
</style>
</head>
<body>
  <article class="card">
    <div class="card__top-band"></div>

    <div class="brand">
      <span class="brand__dot"></span>
      <span class="brand__name">Harwick Legal</span>
    </div>

    <div class="side-block">
      <svg width="46" height="46" viewBox="0 0 46 46" aria-hidden="true">
        <rect width="46" height="46" rx="4" fill="#ffffff"/>
        <circle cx="23" cy="17" r="7" fill="#151515"/>
        <path d="M10 38c1-8 6-12 13-12s12 4 13 12z" fill="#151515"/>
      </svg>
    </div>
    <div class="side-accent"></div>

    <div class="name-band">
      <span class="name-band__name">Marta Greaves</span>
      <span class="name-band__title">General Manager</span>
    </div>

    <div class="contacts">
      <div class="contacts__item">
        <svg width="18" height="18" viewBox="0 0 24 24" aria-hidden="true"><path fill="#151515" d="M6.6 10.8a15 15 0 0 0 6.6 6.6l2.2-2.2a1 1 0 0 1 1-.25 11.4 11.4 0 0 0 3.6.57 1 1 0 0 1 1 1V20a1 1 0 0 1-1 1A17 17 0 0 1 3 4a1 1 0 0 1 1-1h3.5a1 1 0 0 1 1 1c0 1.25.2 2.45.57 3.57a1 1 0 0 1-.25 1z"/></svg>
        <span>012 555 0142</span>
      </div>
      <div class="contacts__item">
        <svg width="18" height="18" viewBox="0 0 24 24" aria-hidden="true"><rect x="2" y="5" width="20" height="14" rx="1" fill="#151515"/><path d="M3 6l9 7 9-7" stroke="#fff" stroke-width="1.6" fill="none"/></svg>
        <span>marta@harwicklegal.example</span>
      </div>
      <div class="contacts__item">
        <svg width="18" height="18" viewBox="0 0 24 24" aria-hidden="true"><rect x="6" y="2" width="12" height="20" rx="2" fill="none" stroke="#151515" stroke-width="2"/><circle cx="12" cy="18" r="1.3" fill="#151515"/></svg>
        <span>012 555 0142</span>
      </div>
      <div class="contacts__item">
        <svg width="18" height="18" viewBox="0 0 24 24" aria-hidden="true"><circle cx="12" cy="12" r="10" fill="none" stroke="#151515" stroke-width="2"/><path d="M2 12h20M12 2c3 3 3 17 0 20M12 2c-3 3-3 17 0 20" stroke="#151515" stroke-width="1.6" fill="none"/></svg>
        <span>www.Harwicklegal.example.au</span>
      </div>
    </div>

    <div class="address-band">
      <svg width="18" height="24" viewBox="0 0 18 24" aria-hidden="true"><path fill="#ffffff" d="M9 0a9 9 0 0 0-9 9c0 6.5 9 15 9 15s9-8.5 9-15a9 9 0 0 0-9-9zm0 12.5A3.5 3.5 0 1 1 9 5.5a3.5 3.5 0 0 1 0 7z"/></svg>
      <span>42 Collins Lane, Level 3, Melbourne VIC</span>
    </div>
  </article>
</body>
</html>
```